Dean Hollis Business Card

In addition to my name design (file uploaded), black print on white card stock, e-mail address should be presented as a typical e-mail address, i.e., underlined and in blue ink, the card should include the following information:
Professor of Aviation Technology
Accident Litigation Expert Witness
Master Certificated Flight Instructor

dhollis@vexmail.example
Kestrel Bay, Alaska
(907) 318-5074

```html
<!DOCTYPE html>
<html lang="en">
<head>
<meta charset="utf-8">
<title>Dean Hollis Business Card</title>
<link rel="stylesheet" href="https://fonts.googleapis.com/css2?family=Bebas+Neue&family=Arimo:wght@400&display=swap">
<style>
  :root {
    --backdrop: #cfcdcd;
    --card: #ffffff;
    --ink: #0d0d0d;
    --link: #2f2f9a;
    --silhouette: #d9d9d9;
    --shadow: rgba(0, 0, 0, 0.55);
  }
  html, body {
    margin: 0;
    padding: 0;
    width: 1200px;
    height: 1000px;
    overflow: hidden;
    background: var(--backdrop);
  }
  .business-card {
    position: absolute;
    left: 69px;
    top: 205px;
    width: 1063px;
    height: 590px;
    background: var(--card);
    box-shadow: 0 2px 3px var(--shadow);
    overflow: hidden;
  }
  .plane-art {
    position: absolute;
    left: 650px;
    top: 55px;
    width: 375px;
    height: 520px;
  }
  .holder-name {
    position: absolute;
    left: 94px;
    top: 96px;
    margin: 0;
    font-family: "Bebas Neue", "Oswald", sans-serif;
    font-weight: 400;
    font-size: 99px;
    line-height: 1;
    letter-spacing: 2px;
    color: var(--ink);
    white-space: nowrap;
  }
  .credentials {
    position: absolute;
    left: 95px;
    top: 209px;
    margin: 0;
    padding: 0;
    list-style: none;
    font-family: "Arimo", Arial, sans-serif;
    font-size: 23px;
    line-height: 42.5px;
    color: var(--ink);
    text-transform: uppercase;
  }
  .contact {
    position: absolute;
    left: 94px;
    top: 380px;
    margin: 0;
    font-family: "Arimo", Arial, sans-serif;
    font-size: 23.5px;
    line-height: 34px;
    font-style: normal;
    color: var(--ink);
  }
  .contact a {
    color: var(--link);
    text-decoration: underline;
    text-underline-offset: 3px;
  }
  .contact span { display: block; }
</style>
</head>
<body>
  <section class="business-card">
    <svg class="plane-art" viewBox="0 0 375 520" role="img" aria-label="Large faint airplane silhouette seen from above, flying toward the upper right">
      <defs>
        <radialGradient id="plane-fade" cx="50%" cy="50%" r="55%">
          <stop offset="0%" stop-color="#d9d9d9"/>
          <stop offset="70%" stop-color="#e6e6e6"/>
          <stop offset="100%" stop-color="#ffffff"/>
        </radialGradient>
      </defs>
      <rect width="375" height="520" fill="url(#plane-fade)"/>
    </svg>

    <h1 class="holder-name">Dean E. Hollis</h1>

    <ul class="credentials">
      <li>Professor of Aviation Technology</li>
      <li>Accident Litigation Expert Witness</li>
      <li>Master Certificated Flight Instructor</li>
    </ul>

    <address class="contact">
      <span><a href="mailto:dhollis@vexmail.example">dhollis@vexmail.example</a></span>
      <span>Kestrel Bay, Alaska</span>
      <span>(907) 318-5074</span>
    </address>
  </section>
</body>
</html>
```